Brume vodka

With the logo attached in the subsequent file, a business card that reflects a premium and organic vodka. On the first side, the company logo in large. The names must be included on the back of the card (Miguel Ángel Tomás Ferrandis with the number +34 655 271 389 and Pau Berenguer Casals and +34 677 314 920). The slogan "What binds us" and "Organic and permium vodka" in bold E-mail (brumevodka@mailfield.net); Website www.brumevodkaorg.net

```html
<!DOCTYPE html>
<html lang="en">
<head>
<meta charset="utf-8">
<title>Brume vodka – business card</title>
<link href="https://fonts.googleapis.com/css2?family=Cinzel:wght@400&family=Lato:wght@400;700&display=swap" rel="stylesheet">
<style>
  :root {
    --backdrop: #2a2a2b;
    --card-white: #ffffff;
    --card-black: #141415;
    --ink-grey: #8c8c8c;
    --ink-soft: #a6a6a6;
    --rule: #dcdcdc;
    --slogan: #f2f2f2;
  }
  * { margin: 0; padding: 0; box-sizing: border-box; }
  html, body { width: 1200px; height: 1108px; overflow: hidden; }
  body {
    background: var(--backdrop);
    display: flex;
    align-items: center;
    justify-content: center;
    gap: 70px;
  }
  .card {
    width: 360px;
    height: 560px;
    border-radius: 24px;
    position: relative;
    box-shadow: 0 18px 40px rgba(0,0,0,0.45);
  }
  .card--front {
    background: var(--card-white);
    display: flex;
    flex-direction: column;
    align-items: center;
    padding: 0 34px;
  }
  .brand-name {
    margin-top: 150px;
    font-family: "Cinzel", serif;
    font-weight: 400;
    font-size: 46px;
    line-height: 1.1;
    color: var(--ink-soft);
    text-align: center;
    letter-spacing: 1px;
  }
  .contacts {
    margin-top: 70px;
    width: 100%;
    font-family: "Lato", sans-serif;
    text-align: center;
    color: var(--ink-grey);
  }
  .contact { padding: 8px 0; border-bottom: 1px solid var(--rule); }
  .contact__name { font-weight: 700; font-size: 16px; text-transform: uppercase; letter-spacing: 0.2px; }
  .contact__phone { font-size: 16px; margin-top: 2px; }
  .contact-web { padding-top: 10px; font-size: 15px; line-height: 1.4; }
  .card--back {
    background: var(--card-black);
  }
  .slogan {
    position: absolute;
    left: 0; right: 0;
    bottom: 70px;
    text-align: center;
    font-family: "Cinzel", serif;
    font-size: 16px;
    line-height: 1.45;
    color: var(--slogan);
    letter-spacing: 0.5px;
  }
</style>
</head>
<body>
  <section class="card card--front" aria-label="Card front">
    <h1 class="brand-name">Brume vodka</h1>
    <div class="contacts">
      <div class="contact">
        <p class="contact__name">Miguel Ángel Tomás Ferrandis</p>
        <p class="contact__phone">+34 655 271 389</p>
      </div>
      <div class="contact">
        <p class="contact__name">Pau Berenguer Casals</p>
        <p class="contact__phone">+34 677 314 920</p>
      </div>
      <div class="contact-web">
        <p>brumevodka@mailfield.net</p>
        <p>www.brumevodkaorg.net</p>
      </div>
    </div>
  </section>

  <section class="card card--back" aria-label="Card back">
    <p class="slogan">What binds us<br>Organic and permium vodka</p>
  </section>
</body>
</html>
```